Progressive/contemporary business card design for successful Startups as a Service Company

New logo launched in 2020. New website launched in 2021. Now that COVID is (mostly) behind us, I'm networking with more people and need a business card that matches the company/logo design aesthetic.

```html
<!DOCTYPE html>
<html lang="en">
<head>
<meta charset="utf-8">
<title>Northvale Business Card</title>
<link href="https://fonts.googleapis.com/css2?family=Montserrat:wght@300&family=Open+Sans:wght@400;700&display=swap" rel="stylesheet">
<style>
  :root {
    --backdrop: #343435;
    --card: #1b1b1c;
    --card-pattern-light: #2a2a2b;
    --card-pattern-dark: #121213;
    --accent-blue: #27a8e0;
    --text-white: #f2f2f2;
    --text-grey: #9a9a9a;
    --icon-pink: #d6338f;
    --icon-green: #6cbf3f;
    --icon-orange: #f08a24;
  }
  * { box-sizing: border-box; margin: 0; padding: 0; }
  html, body {
    width: 1200px; height: 801px; overflow: hidden;
    background: var(--backdrop);
  }
  .card-set {
    position: relative; width: 1200px; height: 801px;
    display: flex; align-items: center; justify-content: center; gap: 40px;
  }
  .card {
    position: relative; width: 540px; height: 309px;
    background: var(--card);
    border-bottom: 4px solid var(--accent-blue);
    box-shadow: 0 12px 30px rgba(0,0,0,.45);
    overflow: hidden;
  }
  .wordmark {
    position: absolute; left: 40px; bottom: 58px;
    font-family: "Montserrat", sans-serif; font-weight: 300;
    font-size: 34px; letter-spacing: 6px;
    color: var(--text-white);
  }
  .contact-block {
    position: absolute; right: 26px; top: 40px;
    width: 244px;
    border-left: 1.5px solid var(--accent-blue);
    border-bottom: 1.5px solid var(--accent-blue);
    padding: 0 0 12px 12px;
    font-family: "Open Sans", sans-serif;
    color: var(--text-white);
    font-size: 12.5px; line-height: 1.45;
  }
  .person-name {
    font-weight: 700; font-size: 19px; color: var(--accent-blue);
    letter-spacing: .3px; line-height: 1.15;
  }
  .person-title { color: var(--text-grey); font-size: 12.5px; margin-bottom: 8px; }
  .address { margin-bottom: 8px; }
  .contact-line { display: flex; align-items: center; gap: 6px; }
  .contact-line svg { width: 11px; height: 11px; flex: none; }
  .pattern-field {
    position: absolute; inset: 0;
    background:
      linear-gradient(135deg, var(--card-pattern-light) 0%, var(--card-pattern-dark) 55%, var(--card-pattern-light) 100%);
  }
  .back-name {
    position: absolute; right: 58px; top: 150px;
    font-family: "Montserrat", sans-serif; font-weight: 300;
    font-size: 20px; letter-spacing: 4px; color: var(--text-white);
  }
</style>
</head>
<body>
<main class="card-set">
  <section class="card card-front">
    <div class="wordmark">NORTHVALE</div>
    <div class="contact-block">
      <div class="person-name">DANA WHITCOMBE</div>
      <div class="person-title">President</div>
      <div class="address">418 W Larkin Ave., Unit B<br>Chicago, IL 60614</div>
      <div class="contact-line">
        <svg viewBox="0 0 12 12" aria-hidden="true"><path fill="var(--icon-pink)" d="M2.5 1h2l1 3-1.3 1a6 6 0 0 0 2.8 2.8L8 6.5l3 1v2c0 .8-.7 1.5-1.5 1.5A8.5 8.5 0 0 1 1 2.5C1 1.7 1.7 1 2.5 1z"/></svg>
        <span>(312) 555-0148</span>
      </div>
      <div class="contact-line">
        <svg viewBox="0 0 12 12" aria-hidden="true"><rect x="1" y="2.5" width="10" height="7" fill="var(--icon-green)"/><path d="M1 2.5l5 4 5-4" stroke="var(--card)" fill="none"/></svg>
        <span>hello@northvaleventures.com</span>
      </div>
      <div class="contact-line">
        <svg viewBox="0 0 12 12" aria-hidden="true"><circle cx="6" cy="6" r="5" fill="var(--icon-orange)"/><path d="M1 6h10M6 1c-2 2.5-2 7.5 0 10M6 1c2 2.5 2 7.5 0 10" stroke="var(--card)" stroke-width=".8" fill="none"/></svg>
        <span>www.northvale.studio</span>
      </div>
    </div>
  </section>
  <section class="card card-back">
    <div class="pattern-field" role="img" aria-label="Embossed black triangular lattice pattern covering the card back"></div>
    <div class="back-name">NORTHVALE</div>
  </section>
</main>
</body>
</html>
```